Small Business Consulting Firm Needs Business Card Design

Need a sleek modern business card with 2 sides matching the colors of our logo. We will be placing these with a mailer we are sending out. These business cards will only ever be given to business owners. We operate helping businesses who are struggling with cash flow or finances. If the green and blue design needs to be moved to the right of "Brightpath Ledger Consulting" for aesthetic purposes that is ok. We will need an editable file if possible. We would like to include the reps name, email, website, and phone number. For now just use Owen Parrish, oparrish@brightpathledger.com, www.brightpathledger.com, and 855-219-7038.

```html
<!DOCTYPE html>
<html lang="en">
<head>
<meta charset="utf-8">
<title>Brightpath Ledger Consulting – Business Card</title>
<link href="https://fonts.googleapis.com/css2?family=Oxygen:wght@300;400;700&display=swap" rel="stylesheet">
<style>
  :root {
    --stage: #141414;
    --card: #1b1b1b;
    --ink: #f2f2f2;
    --muted: #a9a9a9;
    --blue: #0a80c8;
    --green: #6fb83f;
  }
  * { box-sizing: border-box; margin: 0; padding: 0; }
  html, body {
    width: 1200px; height: 1004px; overflow: hidden;
    background: var(--stage);
    font-family: "Oxygen", "Helvetica Neue", Arial, sans-serif;
    color: var(--ink);
  }
  .sheet {
    width: 1200px; height: 1004px;
    display: flex; flex-direction: column; align-items: center; justify-content: center;
    gap: 56px;
  }
  .card {
    position: relative;
    width: 760px; height: 434px;
    background: var(--card);
    box-shadow: 0 14px 40px rgba(0,0,0,.55);
  }

  /* Front */
  .brand { position: absolute; left: 56px; top: 52px; display: flex; align-items: flex-start; gap: 14px; }
  .brand-square { width: 22px; height: 22px; background: var(--green); margin-top: 4px; }
  .brand-name { font-size: 25px; font-weight: 400; letter-spacing: .5px; text-transform: uppercase; line-height: 1.1; }
  .brand-sub { font-size: 11px; letter-spacing: 6px; color: var(--muted); text-transform: uppercase; margin-top: 4px; }

  .address { position: absolute; left: 56px; top: 168px; font-size: 19px; line-height: 1.4; font-weight: 300; }
  .rule { position: absolute; left: 56px; top: 236px; width: 58px; height: 2px; background: var(--green); }
  .contacts { position: absolute; left: 56px; top: 256px; list-style: none; font-size: 19px; font-weight: 300; }
  .contacts li { display: flex; align-items: center; gap: 12px; line-height: 1.55; }
  .contacts svg { width: 15px; height: 15px; flex: none; }
  .accent { color: var(--green); }

  .rep { position: absolute; right: 56px; bottom: 52px; text-align: right; }
  .rep-name { font-size: 30px; font-weight: 400; text-transform: uppercase; letter-spacing: .5px; }
  .rep-first { color: var(--blue); }
  .rep-last { color: var(--green); }
  .rep-title { font-size: 18px; font-weight: 300; color: var(--ink); margin-top: 2px; }

  /* Back */
  .back { display: flex; flex-direction: column; align-items: center; justify-content: center; gap: 34px; }
  .back-brand { display: flex; align-items: center; gap: 18px; }
  .back-brand .brand-square { width: 34px; height: 34px; margin: 0; }
  .back-name { font-size: 38px; font-weight: 400; text-transform: uppercase; letter-spacing: 1px; }
  .back-url { font-size: 20px; letter-spacing: 3px; color: var(--blue); }
</style>
</head>
<body>
<main class="sheet">

  <section class="card front" aria-label="Card front">
    <div class="brand">
      <span class="brand-square"></span>
      <div>
        <div class="brand-name">Brightpath Ledger</div>
        <div class="brand-sub">Consulting</div>
      </div>
    </div>

    <p class="address">1250-640 Harbour Row<br>Lakeview, BC, V2K 4R8</p>
    <span class="rule"></span>

    <ul class="contacts">
      <li>
        <svg viewBox="0 0 16 16" aria-hidden="true"><path fill="var(--blue)" d="M4.2 1.5l2 2.6-1.3 1.6c.9 2 2.4 3.5 4.4 4.4l1.6-1.3 2.6 2-1.3 2.2C7 12.8 3.2 9 2 3.1z"/></svg>
        <span>855-219-7038</span>
      </li>
      <li>
        <svg viewBox="0 0 16 16" aria-hidden="true"><rect x="1" y="3.5" width="14" height="9" fill="var(--blue)"/><path d="M1 3.5l7 5 7-5" fill="none" stroke="var(--card)" stroke-width="1.2"/></svg>
        <span>oparrish@brightpathledger.com</span>
      </li>
      <li>
        <svg viewBox="0 0 16 16" aria-hidden="true"><circle cx="8" cy="8" r="6.5" fill="none" stroke="var(--blue)" stroke-width="1.5"/><path d="M1.5 8h13M8 1.5c-3 3.5-3 9.5 0 13M8 1.5c3 3.5 3 9.5 0 13" fill="none" stroke="var(--blue)" stroke-width="1.2"/></svg>
        <span>www.<span class="accent">brightpathledger</span>.com</span>
      </li>
    </ul>

    <div class="rep">
      <div class="rep-name"><span class="rep-first">Owen</span> <span class="rep-last">Parrish</span></div>
      <div class="rep-title">Owner</div>
    </div>
  </section>

  <section class="card back" aria-label="Card back">
    <div class="back-brand">
      <span class="brand-square"></span>
      <span class="back-name">Brightpath Ledger</span>
    </div>
    <div class="back-url">www.brightpathledger.com</div>
  </section>

</main>
</body>
</html>
```